Net Clarity Partners Needs a New Business Card Design

Attached is my new logo that ArtFolkHub created and picture of me for the back of the business card. Also attached is the information to include on the business card (on my existing business card design - QZR4 file attached).

The designer also provided a treatment of my logo that I really like if you can use it somehow. Also attached - file name "Preferred Version of New Logo."

Maren Falstead

Net Clarity Partners
4517 Pellam Rd., #349
Houston, TX 77348

Tel: (832) 555-0147
www.netclaritypartners.example
maren@netclaritypartners.example

Thank you.

Reason: I'm close but am having a hard time deciding.

Target Market(s)

attorneys and law firms

Industry/Entity Type

Legal

Contact Information for Business Card

Proved in the Project Description

Font styles to use
Other font styles liked:
• I am open on font - no script though.

Colors
2d73b3
33a6d7

Requirements
Must have
• my logo
• company name & contact info
• my picture on the back
• colors that coordinate with the logo
Nice to have
• love to use the treated version of the logo if possible

```html
<!DOCTYPE html>
<html lang="en">
<head>
<meta charset="utf-8">
<title>Net Clarity Partners – Business Card</title>
<link rel="stylesheet" href="https://fonts.googleapis.com/css2?family=Open+Sans:wght@400;600;700&display=swap">
<style>
  :root {
    --stage: #2b2b2b;
    --card-light: #f7f7f7;
    --card-dark: #3b3735;
    --brand-blue: #33a6d7;
    --brand-deep: #2d73b3;
    --text-grey: #666a6e;
    --divider: #c9c9c9;
    --photo-top: #7f766c;
    --photo-mid: #c9a98a;
    --photo-low: #2f3f9c;
  }
  * { margin: 0; padding: 0; box-sizing: border-box; }
  html, body {
    width: 1200px; height: 873px; overflow: hidden;
    background: var(--stage);
    font-family: "Open Sans", Arial, sans-serif;
  }
  .stage {
    position: relative; width: 1200px; height: 873px;
  }
  .card {
    position: absolute; top: 276px;
    width: 560px; height: 320px;
    border-radius: 16px; overflow: hidden;
  }
  .card--front { left: 26px; background: var(--card-light); }
  .card--back { left: 614px; background: var(--card-dark); }

  .wordmark {
    display: flex; align-items: center; gap: 10px;
    font-weight: 700; color: var(--brand-blue);
    text-transform: uppercase; letter-spacing: 1px; white-space: nowrap;
  }
  .wordmark__square { width: 14px; height: 14px; background: var(--brand-deep); flex: none; }

  .card--front .wordmark {
    position: absolute; top: 58px; left: 0; right: 0;
    justify-content: center; font-size: 22px;
  }
  .holder {
    position: absolute; top: 176px; right: 312px; text-align: right;
  }
  .holder__name { font-size: 19px; color: var(--brand-blue); font-weight: 400; }
  .holder__title { font-size: 14px; color: var(--text-grey); margin-top: 4px; }

  .divider {
    position: absolute; left: 272px; top: 138px;
    width: 1px; height: 120px;
    background: linear-gradient(to bottom, transparent, var(--divider) 30%, var(--divider) 70%, transparent);
  }

  .contact {
    position: absolute; left: 296px; top: 140px;
    list-style: none; font-size: 12.5px; color: var(--text-grey);
  }
  .contact li { display: flex; align-items: center; gap: 9px; height: 22px; }
  .contact svg { width: 13px; height: 13px; flex: none; fill: none; stroke: var(--brand-blue); stroke-width: 1.8; }
  .contact__address {
    margin-top: 12px; padding-left: 22px;
    font-size: 13px; font-weight: 700; color: var(--brand-blue); line-height: 1.45;
  }

  .card--back .wordmark {
    position: absolute; left: 30px; top: 192px; font-size: 20px;
  }
  .portrait {
    position: absolute; right: 0; top: 0; width: 250px; height: 100%;
    background: linear-gradient(to bottom, var(--photo-top) 0%, var(--photo-mid) 45%, var(--photo-low) 80%, var(--photo-low) 100%);
  }
</style>
</head>
<body>
<main class="stage">
  <section class="card card--front" aria-label="Business card front">
    <div class="wordmark"><span class="wordmark__square"></span>Net Clarity Partners</div>

    <div class="holder">
      <p class="holder__name">Maren Falstead</p>
      <p class="holder__title">Founder</p>
    </div>

    <div class="divider"></div>

    <ul class="contact">
      <li>
        <svg viewBox="0 0 24 24"><path d="M5 3h4l2 5-2.5 1.5a11 11 0 0 0 6 6L16 13l5 2v4a2 2 0 0 1-2 2A17 17 0 0 1 3 5a2 2 0 0 1 2-2z"/></svg>
        (832) 555-0147
      </li>
      <li>
        <svg viewBox="0 0 24 24"><rect x="3" y="5" width="18" height="14" rx="1"/><path d="M3 6l9 7 9-7"/></svg>
        maren@netclaritypartners.example
      </li>
      <li>
        <svg viewBox="0 0 24 24"><path d="M10 14a4 4 0 0 0 6 0l3-3a4 4 0 0 0-6-6l-1 1"/><path d="M14 10a4 4 0 0 0-6 0l-3 3a4 4 0 0 0 6 6l1-1"/></svg>
        www.netclaritypartners.example
      </li>
      <li class="contact__address" style="display:block;height:auto">4517 Pellam Rd., #349,<br>Houston, TX 77348</li>
    </ul>
  </section>

  <section class="card card--back" aria-label="Business card back">
    <div class="wordmark"><span class="wordmark__square"></span>Net Clarity Partners</div>
    <div class="portrait" role="img" aria-label="Portrait photo of Maren Falstead"></div>
  </section>
</main>
</body>
</html>
```